Physician Flyer

I'm trying to create a one-page flyer, that I can send as a pdf through email. I'd like for it to look very professional and graphically pleasing, but not too heavy so it can email easily. We target the hospital/physician community so it needs to have that type of look/graphics. I have created a piece as an example with my copy, but don't have the expertise to take it further. I have newly revised copy that I can send as well. See example (flyer) with my copy and the second flyer (screenshot) look as just a 'look' example.

Copy to be used on the Flyer:

Recruit
Retain
and Reward

….your most valuable asset

In the competitive world of healthcare, employers now more than ever, need the most advantageous ways to ‘attract and keep’ the highest skilled physicians and reward their loyalty. Most companies insure every aspect of their business, yet fail to insure and secure their most valuable asset. You now can provide the most powerful recruiting and retention tool that rewards your doctors with a no-cost, lifetime tax-free income upon retirement for investing their career with you. This plan is simple, easy to implement and administer with little to no cost.

Provide a benefit the sets you apart - but doesn’t set you back!

Plan Highlights for Hospital:
-Create a significant competitive advantage
-Attract and Recruit world’s top skilled physicians
-Build high retention and loyalty
-Reduce physician turnover
-Total control over plan and plan options
-Leverage assets to reserve cash and revenue
-Life Insurance and ownership on each physician policy

Plan Highlights for Physician:
-Tax-Free Income FOR LIFE upon retirement!
-Millions of Life Insurance protection
-Guaranteed issue, 100% acceptance and approval
-NO medical or financial underwriting
-Critical and chronic illness coverage included
-Zero cost or out of pocket expenses and fees

Plan Features and Highlights:
-The industry’s most significant recruiting and retention tool
-Plan only uses A Rated insurance carriers
-Top experienced banks and funders administrating the program
-Single Application with no individual underwriting or approvals
-Creates a high incentive to stay with employer
-Designed for hospitals, clinics and medical facilities of any size
-Free, fast and simple implementation

For more information contact:

Dorian Pell
512-846-2391
dorianpell@[login to view URL]

```html
<!DOCTYPE html>
<html lang="en">
<head>
<meta charset="utf-8">
<title>Physician Flyer – Recruit, Retain and Reward</title>
<link href="https://fonts.googleapis.com/css2?family=Open+Sans:ital,wght@0,400;0,600;0,700;1,400&family=Roboto+Condensed:ital,wght@0,700;1,400&display=swap" rel="stylesheet">
<style>
  :root{
    --page-bg:#e8e9ec;
    --paper:#f6f4ef;
    --blue:#2a47a0;
    --blue-dark:#1f3a8c;
    --tan:#cdbd8f;
    --tag-gold:#cbb880;
    --ink:#3d3d3d;
    --ink-soft:#555555;
    --logo-blue:#5f7ea8;
  }
  *{box-sizing:border-box;margin:0;padding:0}
  html,body{width:1040px;height:1200px;overflow:hidden}
  body{background:var(--page-bg);font-family:"Open Sans",Arial,sans-serif;position:relative}

  .flyer{position:absolute;left:70px;top:20px;width:900px;height:1160px;background:var(--paper);overflow:hidden;box-shadow:0 6px 22px rgba(0,0,0,.18)}

  .hero-photo{position:absolute;left:0;top:0;width:900px;height:481px;
    background:linear-gradient(100deg,#dfe6ee 0%,#f1f3f6 35%,#e7ecf2 60%,#c9d4e2 100%)}

  .brand-panel{position:absolute;left:0;top:0;width:256px;height:140px;background:rgba(246,246,246,.9);text-align:center}
  .brand-mark{width:68px;height:62px;border-radius:50%;background:var(--logo-blue);margin:12px auto 0}
  .brand-name{font-size:23px;color:#4a4a4a;line-height:1.2;margin-top:2px}
  .brand-tagline{font-size:14px;color:var(--blue);line-height:1.2}

  .headline{position:absolute;left:582px;top:275px;font-family:"Roboto Condensed",Arial,sans-serif;font-weight:700;font-size:40px;line-height:1.12;color:#3b3b3b}
  .headline-tag{position:absolute;left:528px;top:425px;width:310px;height:40px;background:var(--tag-gold);
    font-family:"Roboto Condensed",Arial,sans-serif;font-style:italic;font-size:23px;color:#3b3b3b;line-height:40px;padding-left:10px}

  .intro{position:absolute;left:12px;top:488px;width:876px;font-size:18.6px;line-height:1.3;color:var(--ink)}

  .shapes{position:absolute;left:0;top:0}

  .tagline-band{position:absolute;left:0;top:648px;width:450px;text-align:center;color:#fff;font-size:23px;line-height:1.45}

  .col{position:absolute;top:748px}
  .col-hospital{left:0;width:450px;padding-left:12px}
  .col-features{left:470px;width:420px;padding-left:32px}
  .col h2{font-size:18px;font-weight:700;color:var(--blue);letter-spacing:.3px;margin:6px 0 6px}
  .col-hospital h2 + ul + h2{margin-top:10px}
  .col ul{list-style:none}
  .col li{position:relative;padding-left:34px;font-size:13.4px;line-height:1.22;color:var(--ink-soft);text-transform:uppercase;margin-bottom:1px;padding-right:8px}
  .col li::before{content:"";position:absolute;left:14px;top:4px;width:9px;height:8px;border:1.2px solid #a07e42;border-top:none;border-right:none}
  .col li::after{content:"";position:absolute;left:17px;top:2px;width:7px;height:1.2px;background:#a07e42;transform:rotate(-40deg);transform-origin:left}
  .col-features li{font-size:13.6px;margin-bottom:2px}

  .contact-cta{position:absolute;left:0;top:1099px;width:450px;height:61px;line-height:61px;text-align:center;color:#fff;font-weight:700;font-size:19px}
  .contact-card{position:absolute;left:515px;top:1057px;width:385px;text-align:center;color:#fff;font-size:17.5px;line-height:1.4;text-transform:uppercase}
</style>
</head>
<body>
<main class="flyer">
  <div class="hero-photo" role="img" aria-label="Photo of a team of physicians and nurses in scrubs and white coats gathered around a table in a bright clinic"></div>

  <div class="brand-panel">
    <div class="brand-mark"></div>
    <div class="brand-name">Company Name</div>
    <div class="brand-tagline">Your Heading Here</div>
  </div>

  <h1 class="headline">Recruit<br>Retain<br>and Reward</h1>
  <div class="headline-tag">......your most valuable asset</div>

  <p class="intro">In the competitive world of healthcare, employers now more than ever, need the most advantageous ways to ‘attract and keep’ the highest skilled physicians and reward their loyalty. Most companies insure every aspect of their business, yet fail to insure and secure their most valuable asset. You now can provide the most powerful recruiting and retention tool that rewards your doctors with a no-cost, lifetime tax-free income upon retirement for investing their career with you. This plan is simple, easy to implement and administer with little to no cost.</p>

  <svg class="shapes" width="900" height="1160" viewBox="0 0 900 1160" aria-hidden="true">
    <rect x="0" y="742" width="450" height="357" fill="var(--tan)"/>
    <polygon points="0,644 450,644 515,644 900,644 900,729 515,729 450,742 0,742" fill="var(--blue)"/>
    <polygon points="450,644 515,644 515,729 450,742" fill="var(--blue-dark)"/>
    <polygon points="515,1049 900,1049 900,1148 515,1148" fill="var(--blue)"/>
    <polygon points="0,1099 450,1099 515,1049 515,1148 450,1160 0,1160" fill="var(--blue)"/>
    <polygon points="450,1099 515,1049 515,1148 450,1160" fill="var(--blue-dark)"/>
  </svg>

  <p class="tagline-band">Provide a benefit the sets you apart -<br>but doesn’t set you back!</p>

  <section class="col col-hospital">
    <h2>PLAN HIGHLIGHTS FOR HOSPITAL:</h2>
    <ul>
      <li>Create a significant competitive advantage</li>
      <li>Attract and recruit world’s top skilled physicians</li>
      <li>Build high retention and loyalty</li>
      <li>Reduce physician turnover</li>
      <li>Total control over plan and plan options</li>
      <li>Leverage assets to reserve cash and revenue</li>
      <li>Life insurance and ownership on each physician policy</li>
    </ul>
    <h2>PLAN HIGHLIGHTS FOR PHYSICIAN:</h2>
    <ul>
      <li>Tax-free income for life upon retirement!</li>
      <li>Millions of life insurance protection</li>
      <li>Guaranteed issue, 100% acceptance and approval</li>
      <li>No medical or financial underwriting</li>
      <li>Critical and chronic illness coverage included</li>
      <li>Zero cost or out of pocket expenses and fees</li>
    </ul>
  </section>

  <section class="col col-features">
    <h2>PLAN FEATURES AND HIGHLIGHTS:</h2>
    <ul>
      <li>The industry’s most significant recruiting and retention tool</li>
      <li>Plan only uses A rated insurance carriers</li>
      <li>Top experienced banks and funders administrating the program</li>
      <li>Single application with no individual underwriting or approvals</li>
      <li>Creates a high incentive to stay with employer</li>
      <li>Designed for hospitals, clinics and medical facilities of any size</li>
      <li>Free, fast and simple implementation</li>
    </ul>
  </section>

  <p class="contact-cta">FOR MORE INFORMATION CONTACT</p>
  <address class="contact-card" style="font-style:normal">
    Dorian Pell<br>
    512-846-2391<br>
    dorianpell@[login to view URL]
  </address>
</main>
</body>
</html>
```